Powerpoint Template for Database Technology Firm

We would like some custom branding for our powerpoint slides. We do many presentations and we would like to extend our brand through the powerpoint slides.

The two main colors are RGB 49 118 181 and RGB 217 179 40. Please build the deck in the 16:9 ratio.

The 'starting' or main screen can show lots of color and can be exciting; however, the body of the presentation should be reserved so the content will be the focus. The header should be minimal and simple; however, we would like something more than just a rectangle of the same color. We would like the attached logo on the detail page in the footer area.

We would like a biography page where we can put information about the speaker along with the contact information. A plimbo logo and a email icon could be used here.

We are also looking a final page for questions or wrap up. This page can also be more 'fun'.

This hopefully explains the slides I am looking for
- opening/starting slide
- A biography slide
- content slides (it will be nice to see different layouts, image/text, two text sections, image description)
- A questions/closing slide

There is no specific text I am looking for as it will change every time. You can use the name of the company on the starter slide and fill the rest with example images/lorem text.

Target Market(s)

Attendees to a conference or webinar.

Industry/Entity Type

Information Technology

Requirements
Must have
• simple content pages with logo and branding included.
• Consistent use of colors
• I would like a header and a footer, but the header can be very simple. Maybe several squares with yellow/blue blocks. I am less interested in lines in the header.
Should not have
• content pages should not distract from the content.

```html
<!DOCTYPE html>
<html lang="en">
<head>
<meta charset="utf-8">
<title>Corvane Data – Slide Template</title>
<link rel="stylesheet" href="https://fonts.googleapis.com/css2?family=Open+Sans:wght@400;600;700;800&display=swap">
<style>
  :root {
    --brand-blue: #3176b5;
    --brand-blue-dark: #23609a;
    --brand-yellow: #d9b328;
    --ink: #111418;
    --paper: #ffffff;
    --canvas: #eef1f5;
    --ring: rgba(255,255,255,0.16);
  }
  * { box-sizing: border-box; margin: 0; padding: 0; }
  html, body { width: 849px; height: 1200px; overflow: hidden; }
  body { background: var(--canvas); font-family: "Open Sans", Arial, sans-serif; color: var(--ink); position: relative; }

  .slide { position: absolute; left: 28px; width: 793px; height: 566px; overflow: hidden; box-shadow: 0 1px 4px rgba(0,0,0,0.18); }
  .slide--content { top: 14px; background: var(--paper); }
  .slide--closing { top: 608px; background: var(--brand-blue); }

  .slogan-bar { position: absolute; top: 14px; left: 0; height: 30px; width: 226px; background: var(--brand-blue); color: var(--paper); font-size: 12px; font-weight: 600; line-height: 30px; padding-left: 14px; }
  .slogan-bar::before { content: ""; position: absolute; left: 0; top: 0; width: 5px; height: 100%; background: var(--brand-yellow); }
  .slide--closing .slogan-bar { background: var(--brand-blue-dark); }

  .ring-decor { position: absolute; top: -120px; right: -110px; width: 360px; height: 360px; border-radius: 50%; background: var(--ring); }
  .slide--content .ring-decor { background: rgba(49,118,181,0.06); }

  .slide-title { position: absolute; top: 84px; left: 50px; font-size: 40px; font-weight: 800; letter-spacing: -0.5px; }
  .columns { position: absolute; top: 158px; left: 50px; right: 30px; display: grid; grid-template-columns: 1fr 1fr; column-gap: 26px; font-size: 12.5px; line-height: 17px; }

  .footer { position: absolute; left: 0; right: 0; bottom: 0; height: 56px; display: flex; }
  .footer-brand { width: 190px; background: var(--paper); display: flex; align-items: center; gap: 8px; padding-left: 30px; color: var(--brand-blue); font-weight: 800; font-size: 17px; }
  .footer-brand .mark { width: 14px; height: 14px; background: var(--brand-yellow); }
  .footer-band { flex: 1; background: var(--brand-yellow); color: var(--paper); font-size: 12px; font-weight: 600; display: flex; align-items: center; justify-content: flex-end; padding-right: 30px; }

  .thanks { position: absolute; top: 92px; left: 60px; color: var(--paper); font-size: 44px; font-weight: 700; }
  .contact { position: absolute; top: 180px; left: 150px; color: var(--paper); font-size: 15px; line-height: 21px; }
  .contact h3 { font-size: 16px; font-weight: 700; margin-top: 18px; }
</style>
</head>
<body>

<section class="slide slide--content">
  <div class="ring-decor"></div>
  <div class="slogan-bar">Presentation slogan here</div>
  <h1 class="slide-title">Two column matter</h1>
  <div class="columns">
    <p>The 'starting' or main screen can show lots of color and can be exciting; however, the body of the presentation should be reserved so the content will be the focus. The header should be minimal and simple; however, we would like something more than just a rectangle of the same color. We would like the attached logo on the detail page in the footer area. The 'starting' or main screen can show lots of color and can be exciting; however, the body of the presentation should be reserved so the content will be the focus. The header should be minimal and simple; however, we would like something more than The 'starting' or main screen can show lots of color and can be exciting; however, the body of the presentation should be reserved so the content will be the focus. The header should be minimal and simple; however, we</p>
    <p>would like something more than just a rectangle of the same color. We would like the attached logo on the detail page in the footer area. The 'starting' or main screen can show lots of color and can be exciting; however, the body of the presentation should be reserved so the content will be the focus. The header should be minimal and simple; however, we would like something more than just a rectangle of the same color. We would like the attached logo on the detail page in the footer area. The 'starting' or main screen can show lots of color and can be exciting; however, the body of the presentation should be reserved so the content will be the focus. The header should be minimal and simple; however, we would like something more than just a rectangle of the same color. We would like the attached logo on the detail page in the footer area. The 'starting' or main screen can show lots of color and can be exciting; however, the body of the presentation should be reserved so the</p>
  </div>
  <footer class="footer">
    <div class="footer-brand"><span class="mark"></span>Corvane</div>
    <div class="footer-band">www.corvanedata.com</div>
  </footer>
</section>

<section class="slide slide--closing">
  <div class="ring-decor"></div>
  <div class="slogan-bar">Presentation slogan here</div>
  <h1 class="thanks">Thank you</h1>
  <div class="contact">
    <p>Mr. ABC SURNAME<br>Your contact details<br>Your address in details<br>Comes here</p>
    <h3>Contact details:</h3>
    <p>Office phone : 0144 555 0190<br>Mobile : 0166 555 0132<br>fax no: 044-555-0178<br>E-id: www.corvanemail.com</p>
  </div>
  <footer class="footer">
    <div class="footer-brand"><span class="mark"></span>Corvane</div>
    <div class="footer-band">www.corvanedata.com</div>
  </footer>
</section>

</body>
</html>
```